Brochure Design

We need a 6 page Brochure designed for our product, please see attached document for more information. The content should focus on account work.

Target Market(s)

Businesses that use a taxi service for their business

Requirements
Must have
• Must have key content on the services we provide for Account work

```html
<!DOCTYPE html>
<html lang="en">
<head>
<meta charset="utf-8">
<title>Vexo Business Travel Brochure</title>
<link href="https://fonts.googleapis.com/css2?family=Oswald:wght@400;500;600&family=Lato:wght@400;700&display=swap" rel="stylesheet">
<style>
  :root{
    --yellow:#f4b631;
    --yellow-light:#f9cf6a;
    --charcoal:#232323;
    --charcoal-2:#3a3a3a;
    --white:#ffffff;
    --text:#3c3c3c;
    --muted:#6b6b6b;
    --stage-light:#e4e4e4;
    --stage-mid:#a9a9a9;
  }
  *{box-sizing:border-box;margin:0;padding:0}
  html,body{width:768px;height:1200px;overflow:hidden}
  body{background:var(--stage-light);font-family:"Lato",sans-serif;color:var(--text);position:relative}

  .band{position:absolute;left:0;width:768px}
  .band--cover{top:0;height:520px;background:var(--stage-light)}
  .band--outside{top:520px;height:340px;background:var(--stage-mid)}
  .band--inside{top:860px;height:340px;background:var(--stage-light)}

  .cover{position:absolute;left:184px;top:60px;width:400px;height:401px;overflow:hidden;box-shadow:0 10px 30px rgba(0,0,0,.25)}
  .cover__inner{position:absolute;left:0;top:0;width:274px;height:275px;transform:scale(1.46);transform-origin:0 0}

  .spread{position:absolute;left:20px;top:48px;width:728px;height:244px;overflow:hidden;box-shadow:0 6px 18px rgba(0,0,0,.18)}
  .spread__inner{position:absolute;left:0;top:0;width:822px;height:275px;transform:scale(.8856);transform-origin:0 0}
  .art{position:absolute;inset:0;width:100%;height:100%}
  .abs{position:absolute}

  .headline{font-family:"Oswald",sans-serif;font-weight:500;text-transform:uppercase;line-height:1.08;letter-spacing:-.2px}
  .headline__accent{color:var(--yellow)}
  .headline__main{color:var(--white)}

  .brand-mark{display:flex;align-items:center;gap:6px;font-family:"Oswald",sans-serif;font-weight:600;color:var(--charcoal);text-transform:lowercase}
  .brand-mark__dot{border-radius:50%;background:var(--charcoal)}

  .intro{left:31px;top:17px;width:212px;font-size:6.4px;line-height:1.35;color:var(--text)}
  .intro p+p{margin-top:7px}

  .url{font-size:7.5px;letter-spacing:.3px}
  .url--dark{color:var(--charcoal-2)}
  .url--light{color:#d8d8d8}

  .contact{left:283px;top:208px;font-size:8px;color:var(--charcoal)}
  .contact li{list-style:none;display:flex;align-items:center;gap:4px;height:15px}
  .contact__icon{width:9px;height:9px;border-radius:50%;background:var(--charcoal);border:1.5px solid var(--yellow)}
  .store-badge{width:52px;height:16px;border-radius:3px;background:#111;border:1px solid #777}

  .feature__title{font-family:"Oswald",sans-serif;font-weight:500;font-size:8.5px;text-transform:uppercase;color:var(--charcoal)}
  .feature__title span{color:var(--yellow)}
  .feature__text{font-size:6.4px;line-height:1.3;color:var(--muted);margin-top:4px}

  .checklist{font-size:6.3px;line-height:1.3;color:var(--muted)}
  .checklist li{list-style:none;position:relative;padding-left:12px}
  .checklist li::before{content:"";position:absolute;left:0;top:0;width:7px;height:7px;border-radius:50%;background:var(--yellow)}
  .checklist li::after{content:"";position:absolute;left:2px;top:1.8px;width:3px;height:1.6px;border-left:1px solid var(--white);border-bottom:1px solid var(--white);transform:rotate(-45deg)}

  .product__title{font-family:"Oswald",sans-serif;font-weight:500;font-size:8.5px;color:var(--white);text-transform:uppercase}
  .product__title span{color:var(--yellow)}
  .product__item{position:absolute;left:668px;width:135px;font-size:6.3px;line-height:1.3;color:#d6d6d6;padding-left:26px}
  .product__icon{position:absolute;left:0;top:0;width:18px;height:18px}
</style>
</head>
<body>

<!-- Front cover, flat -->
<section class="band band--cover">
  <div class="cover">
    <div class="cover__inner">
      <svg class="art" viewBox="0 0 274 275" preserveAspectRatio="none">
        <defs>
          <linearGradient id="coverPhoto" x1="0" y1="0" x2="1" y2="1">
            <stop offset="0" stop-color="#3b3540"/>
            <stop offset=".55" stop-color="#5c4160"/>
            <stop offset="1" stop-color="#8a6a70"/>
          </linearGradient>
        </defs>
        <rect width="274" height="275" fill="#232323"/>
        <path role="img" aria-label="Night street photo with a lit taxi roof sign" d="M0 0H274V190L0 120Z" fill="url(#coverPhoto)"/>
        <path d="M0 150L274 214V232L0 168Z" fill="#f4b631"/>
        <path d="M0 172L274 236V246L0 182Z" fill="#c7922a"/>
        <polygon points="92,26 160,65 160,143 92,182 24,143 24,65" fill="#f4b631"/>
      </svg>
      <div class="abs brand-mark" style="left:62px;top:90px;font-size:28px"><span class="brand-mark__dot" style="width:14px;height:14px"></span>vexo</div>
      <div class="abs headline" style="left:22px;top:212px;font-size:19px">
        <div class="headline__accent">Exceptional Travel</div>
        <div class="headline__main">For a Modern Business</div>
      </div>
    </div>
  </div>
</section>

<!-- Outside spread -->
<section class="band band--outside">
  <div class="spread">
    <div class="spread__inner">
      <svg class="art" viewBox="0 0 822 275" preserveAspectRatio="none">
        <defs>
          <linearGradient id="outsidePhoto" x1="0" y1="0" x2="1" y2=".6">
            <stop offset="0" stop-color="#2e2e2e"/>
            <stop offset=".55" stop-color="#3f3a44"/>
            <stop offset="1" stop-color="#7b5e6e"/>
          </linearGradient>
        </defs>
        <rect width="822" height="275" fill="#ffffff"/>
        <path role="img" aria-label="Car interior at night with a taxi roof sign" d="M306 0H822V275H496Z" fill="url(#outsidePhoto)"/>
        <path d="M264 0H290L480 275H454Z" fill="#f9cf6a"/>
        <path d="M290 0H306L496 275H480Z" fill="#f4b631"/>
        <path d="M0 112L150 275H0Z" fill="#f4b631"/>
        <path d="M66 200H82L150 275H134Z" fill="#2a2a2a"/>
        <path d="M82 200H96L164 275H150Z" fill="#5a5a5a"/>
        <path d="M470 275L560 178H730L800 275Z" fill="#222222"/>
        <path d="M748 210H768L822 275H802Z" fill="#f4b631"/>
        <path d="M770 210H782L836 275H824Z" fill="#c7922a"/>
        <polygon points="598,36 662,73 662,147 598,184 534,147 534,73" fill="#f4b631"/>
        <rect role="img" aria-label="Two phones showing the booking app map" x="147" y="140" width="88" height="113" rx="8" fill="#d9d9d9"/>
        <rect x="152" y="146" width="38" height="102" rx="4" fill="#f4b631" opacity=".55"/>
        <rect x="196" y="152" width="34" height="94" rx="4" fill="#f4b631" opacity=".4"/>
      </svg>

      <div class="abs intro">
        <p>Your business can't wait, but it shouldn't compromise on quality. A Vexo Business Account guarantees an executive vehicle in London; with 4G Wi-Fi and phone chargers in every vehicle, you can stay connected to your business every step of your journey.</p>
        <p>Take full control of your business travel with the Vexo Dispatch Portal, which helps you manage bookings, users, and finances in one space. Plus, with a dedicated account manager, you'll have access to 24/7 support should you need it.</p>
        <p>Open a business account today and take advantage of our executive services outside of London; whether your business travel takes you across the London, Europe, UAE, or Asia.</p>
      </div>

      <div class="abs url url--dark" style="left:15px;top:241px">www.vexo.cab</div>

      <ul class="abs contact">
        <li><span class="contact__icon"></span>+1(555) 014 2290</li>
        <li><span class="contact__icon"></span>hello@vexo.cab</li>
        <li><span class="contact__icon"></span>www.vexo.cab</li>
      </ul>
      <div class="abs store-badge" style="left:380px;top:213px"></div>
      <div class="abs store-badge" style="left:380px;top:234px"></div>

      <div class="abs brand-mark" style="left:566px;top:92px;font-size:24px"><span class="brand-mark__dot" style="width:11px;height:11px"></span>vexo</div>
      <div class="abs headline" style="left:566px;top:208px;font-size:15px">
        <div class="headline__accent">Exceptional Travel</div>
        <div class="headline__main">For a Modern Business</div>
      </div>
    </div>
  </div>
</section>

<!-- Inside spread -->
<section class="band band--inside">
  <div class="spread">
    <div class="spread__inner">
      <svg class="art" viewBox="0 0 822 275" preserveAspectRatio="none">
        <defs>
          <linearGradient id="driverPhoto" x1="0" y1="0" x2="1" y2="1">
            <stop offset="0" stop-color="#2a2a30"/>
            <stop offset=".6" stop-color="#4a3f4a"/>
            <stop offset="1" stop-color="#6e5a60"/>
          </linearGradient>
          <linearGradient id="panelPhoto" x1="0" y1="0" x2="1" y2="1">
            <stop offset="0" stop-color="#1f1f1f"/>
            <stop offset="1" stop-color="#363636"/>
          </linearGradient>
        </defs>
        <rect width="822" height="275" fill="#ffffff"/>
        <path d="M0 0H60L0 80Z" fill="#232323"/>
        <path d="M0 170L100 275H0Z" fill="#232323"/>
        <path d="M92 240H110L140 275H122Z" fill="#232323"/>
        <path d="M122 240H140L170 275H152Z" fill="#f4b631"/>
        <path d="M140 240H152L182 275H170Z" fill="#f9cf6a"/>
        <path d="M245 0H262L357 137H340Z" fill="#f9cf6a"/>
        <path d="M262 0H270L365 137H357Z" fill="#f4b631"/>
        <path role="img" aria-label="Driver's hand on a steering wheel at night" d="M270 0H461L555 137H365Z" fill="url(#driverPhoto)"/>
        <path role="img" aria-label="Dark taxi roof sign photo" d="M461 0H822V275H651Z" fill="url(#panelPhoto)"/>
        <path d="M790 0H822V45Z" fill="#f4b631"/>
        <path d="M545 150H560L647 275H632Z" fill="#f4b631"/>
        <path d="M562 150H571L658 275H649Z" fill="#f9cf6a"/>

        <g fill="#f4b631" stroke="#232323" stroke-width="3">
          <polygon points="36,37 62,52 62,82 36,97 10,82 10,52"/>
          <polygon points="66,107 92,122 92,152 66,167 40,152 40,122"/>
          <polygon points="98,177 124,192 124,222 98,237 72,222 72,192"/>
        </g>
        <g fill="none" stroke="#232323" stroke-width="2">
          <circle cx="36" cy="67" r="13"/>
        </g>
        <text x="36" y="71" text-anchor="middle" font-family="Oswald, sans-serif" font-size="10" font-weight="600" fill="#232323">24/7</text>
        <path d="M66 126a9 9 0 0 1 9 9c0 7-9 16-9 16s-9-9-9-16a9 9 0 0 1 9-9z" fill="#232323"/>
        <circle cx="66" cy="135" r="3.3" fill="#f4b631"/>
        <path d="M84 213h28v-6l-4-8h-20l-4 8z" fill="#232323"/>
        <circle cx="90" cy="214" r="3" fill="#232323"/>
        <circle cx="106" cy="214" r="3" fill="#232323"/>
        <rect x="94" y="192" width="8" height="5" fill="#232323"/>

        <rect role="img" aria-label="Phone showing the booking app screen" x="572" y="20" width="84" height="170" rx="10" fill="#111111" stroke="#555" stroke-width="1.5"/>
        <rect x="577" y="36" width="74" height="134" fill="#f4b631"/>
        <circle cx="614" cy="180" r="5" fill="none" stroke="#555"/>

        <g fill="none" stroke="#f4b631" stroke-width="1.4">
          <path d="M670 78l6-6m-3 9l-3 3a4 4 0 0 1-6-6l3-3m6-6l3-3a4 4 0 0 1 6 6l-3 3"/>
          <rect x="668" y="136" width="12" height="10" rx="1.5"/>
          <path d="M670 136v-4a4 4 0 0 1 8 0v4"/>
          <path d="M666 194c3-5 9-5 12-0c-3 5-9 5-12 0z"/>
          <circle cx="672" cy="194" r="2"/>
        </g>
      </svg>

      <div class="abs" style="left:79px;top:50px;width:180px">
        <div class="feature__title"><span>24/7</span> Support</div>
        <div class="feature__text">Our Account Management Team and support 24/7/365 from our HQ in London</div>
      </div>
      <div class="abs" style="left:106px;top:120px;width:160px">
        <div class="feature__title"><span>Average 7 min</span> pick ups</div>
        <div class="feature__text">Benefit from a priority service ensuring we are only ever moments away</div>
      </div>
      <div class="abs" style="left:138px;top:190px;width:130px">
        <div class="feature__title"><span>Trained hand</span> picked drivers</div>
        <div class="feature__text">Our drivers are trained and vetted to ensure high service, quality and safety</div>
      </div>

      <div class="abs url url--light" style="left:15px;top:241px">www.vexo.cab</div>

      <ul class="abs checklist" style="left:283px;top:160px;width:125px">
        <li style="margin-bottom:9px">Cost effective service with quality vehicles</li>
        <li style="margin-bottom:9px">Dedicated Access via online system</li>
        <li style="margin-bottom:9px">Bookings can be made quickly and simply</li>
        <li style="margin-bottom:9px">Phone Support when needed, 24x7</li>
        <li>Advanced Booking options</li>
      </ul>
      <ul class="abs checklist" style="left:415px;top:160px;width:125px">
        <li style="margin-bottom:9px">Regular repeat scheduled Booking options</li>
        <li style="margin-bottom:9px">Airport Transfers</li>
        <li style="margin-bottom:9px">Mid-range to Executive vehicles</li>
        <li>Your entry point to the UK-wide Vexo network</li>
      </ul>

      <div class="abs product__title" style="left:668px;top:30px"><span>Product</span> Features</div>
      <div class="product__item" style="top:50px">Safety features where a passenger can send a link to any contact for them to track the ride real time.</div>
      <div class="product__item" style="top:100px">Drivers thoroughly vetted including the enhanced disclosure and barring system, ensuring the highest level of safety checks available for the passengers.</div>
      <div class="product__item" style="top:160px">Customer benefits as there is no surge pricing.</div>
    </div>
  </div>
</section>

</body>
</html>
```